Business Card Design and Basic Text Logo

We are looking for a business card design for an e-business company. Our business is the parent company of a few website businesses. The final logo and business card design will communicate a conservative but modern and expansive business

The Logo text is: 87Merchant
We would also like a basic text logo design for 87Merchant. The logo could also fill up the reverse side of the business card.

The colours we would like to use are:
White
Navy
Black

This is the text that will be added to the card:

Dean Colley
Business Development Manager

Phone: +61 417 658 294
Email: dean.colley@87merchant.com.au

Industry/Entity Type

Business

Logo Text

87Merchant

Logo styles of interest
Pictorial/Combination Logo
Requirements
Must have
• Modern and attractive design
Nice to have
• communicate a conservative but modern and expansive business
Should not have
• Should be too dull and plan
• But also should be overly colourful

```html
<!DOCTYPE html>
<html lang="en">
<head>
<meta charset="utf-8">
<title>87Merchant Business Card</title>
<link href="https://fonts.googleapis.com/css2?family=Open+Sans:wght@400;600&display=swap" rel="stylesheet">
<style>
  :root {
    --backdrop: #34413f;
    --card: #fbfbfb;
    --navy: #1c2a4f;
    --ink: #2b2b2b;
    --muted: #555a60;
    --faint: #e4e4e4;
  }
  html, body {
    margin: 0;
    width: 1200px;
    height: 1000px;
    overflow: hidden;
    background: var(--backdrop);
    font-family: "Open Sans", Arial, sans-serif;
  }
  .stage {
    width: 1200px;
    height: 1000px;
    display: flex;
    flex-direction: column;
    align-items: center;
    justify-content: center;
    gap: 70px;
  }
  .card {
    position: relative;
    width: 620px;
    height: 354px;
    background: var(--card);
    overflow: hidden;
    box-shadow: 0 10px 28px rgba(0,0,0,0.35);
  }
  .wordmark {
    color: var(--navy);
    font-weight: 600;
    letter-spacing: 0.5px;
    white-space: nowrap;
  }
  .card-front .wordmark {
    position: absolute;
    left: 48px;
    top: 52px;
    font-size: 40px;
  }
  .corner-accent {
    position: absolute;
    right: -70px;
    top: -70px;
    width: 230px;
    height: 230px;
    border-radius: 50%;
    background: var(--faint);
  }
  .holder {
    position: absolute;
    left: 120px;
    top: 132px;
  }
  .holder-name {
    font-size: 22px;
    color: var(--muted);
    margin: 0;
  }
  .holder-title {
    font-size: 14px;
    color: var(--navy);
    margin: 2px 0 0;
  }
  .contact-list {
    position: absolute;
    left: 120px;
    top: 216px;
    list-style: none;
    margin: 0;
    padding: 0;
    font-size: 13px;
    color: var(--ink);
  }
  .contact-list li {
    display: flex;
    align-items: center;
    gap: 12px;
    height: 24px;
  }
  .contact-icon {
    width: 14px;
    height: 14px;
    flex: none;
  }
  .card-back {
    display: flex;
    align-items: center;
    justify-content: center;
  }
  .card-back .wordmark {
    font-size: 64px;
  }
</style>
</head>
<body>
<main class="stage">
  <section class="card card-front" aria-label="Card front">
    <div class="corner-accent" aria-hidden="true"></div>
    <div class="wordmark">87Merchant</div>
    <div class="holder">
      <p class="holder-name">Dean Colley</p>
      <p class="holder-title">Business Development Manager</p>
    </div>
    <ul class="contact-list">
      <li>
        <svg class="contact-icon" viewBox="0 0 14 14" aria-hidden="true"><path d="M3 1 L5.5 1 L6.5 4 L5 5.2 Q6.2 8 8.8 9 L10 7.5 L13 8.5 L13 11 Q12.5 13 10.5 13 Q1 11 1 3.5 Q1 1.5 3 1 Z" fill="#2b2b2b"/></svg>
        <span>+61 417 658 294</span>
      </li>
      <li>
        <svg class="contact-icon" viewBox="0 0 14 14" aria-hidden="true"><rect x="0.5" y="2.5" width="13" height="9" fill="#2b2b2b"/><path d="M1 3 L7 8 L13 3" stroke="#fbfbfb" stroke-width="1.2" fill="none"/></svg>
        <span>dean.colley@87merchant.com.au</span>
      </li>
      <li>
        <svg class="contact-icon" viewBox="0 0 14 14" aria-hidden="true"><circle cx="7" cy="7" r="6.5" fill="#2b2b2b"/><ellipse cx="7" cy="7" rx="2.6" ry="6.2" stroke="#fbfbfb" stroke-width="0.9" fill="none"/><path d="M1 7 H13" stroke="#fbfbfb" stroke-width="0.9"/></svg>
        <span>www.87merchant.com.au</span>
      </li>
    </ul>
  </section>
  <section class="card card-back" aria-label="Card back">
    <div class="wordmark">87Merchant</div>
  </section>
</main>
</body>
</html>
```